Brand Packaging Identity H
ZOLT WATCHES
Dear Designers,
Thanks everyone for there contribution and efforts, we shall finalize the project in a day.
Many thanks once again,
Regards,
PH
Thank you
have you decided yet?
LAST 2 days to go...
Goodluck,
The project has been extended for 4 days more, please understand our requirements and post your drafts.
Thanks,
#90 Please use original brand identity in your designs.
The project has been extended for 4 days, please submit your designs and we hope you'll meet the expectations.
Thank you all for your efforts, the contest will be over in next 10 hours. Please recharge your enthusiasm and strike your new ideas in new designs.
All the best,
Please be different in Watch Gift Box designing and Watch Tags designing, its not just an identical design on every item but its about creating new standards and new styles for a better usage. So, please be creative and innovative, all submitted drafts have almost similar stuff with a difference in design and art. Please add new and fresh ideas.
All goodluck, JUST ONE DAY TO GO.
Come'on Designers Buck up, its just 2 days more... send your designs and get over it.
#49: Please use the exact identity in your designs and instead of black gray could be a nicer combination.
Also try in another design combination near to the requirements.
#64: One star for the watch Pad and polybag, other identities could be much better please make it more appealing.
Rgds.,
#67: Zolt is a trendy digital watch, we appreciate your efforts, could be better.
the project has been extended for 3 days, please submit your designs soon.
Hello Ph,
Please check your private message at upper right corner.
#50: Zolt is a trendy digital watch.
Please be innovative in your work, there could be much better designs that draws better impact to the mind and leaves a lasting impression. Please submit those designs.
JUST A DAY TO GO...
Goodluck ALL,
#43: made it so simple, please be unique remember its a trendy digital watch, fresh ideas will be appreciated.
#44: You are a bit creative, but please use light colors in your designs, we value your efforts.
#45: We are looking for light color identity, your designs are good but would be much better if light background was used.
lets be active and make your creativity and concepts flow in designs.
Goodluck everyone,
rgds.,
The project has been extended for 3 days, please submit your fresh designs soon.

```html
<!DOCTYPE html>
<html lang="en">
<head>
<meta charset="utf-8">
<title>Zolt Watches – Packaging Identity</title>
<link href="https://fonts.googleapis.com/css2?family=Exo+2:wght@400;700;800&display=swap" rel="stylesheet">
<style>
:root{
  --bg:#3b3b3c;
  --blue-light:#3fb6ee;
  --blue:#1c9ad9;
  --blue-deep:#0a70b6;
  --navy:#0d2438;
  --white:#ffffff;
  --paper:#eef3f6;
}
*{box-sizing:border-box;margin:0;padding:0}
html,body{width:1200px;height:847px;overflow:hidden;background:var(--bg)}
body{position:relative;font-family:"Exo 2",sans-serif;color:var(--white)}
.piece{position:absolute}
.blue{background:linear-gradient(135deg,var(--blue-light),var(--blue) 55%,var(--blue-deep))}
.brand{font-family:"Exo 2",sans-serif;font-weight:800;color:var(--navy);letter-spacing:1px;line-height:1;position:absolute;white-space:nowrap}
.url{position:absolute;font-size:9px;font-weight:700;color:var(--white);letter-spacing:.5px;white-space:nowrap}
.fine{position:absolute;font-size:6px;color:rgba(255,255,255,.55);line-height:1.4}

/* gift box dieline */
.gift-main{left:91px;top:72px;width:192px;height:312px;border:1px solid rgba(255,255,255,.5)}
.gift-flap-l{left:34px;top:84px;width:57px;height:290px;border:1px solid rgba(255,255,255,.5);overflow:hidden}
.gift-flap-r{left:283px;top:84px;width:41px;height:290px;border:1px solid rgba(255,255,255,.5)}
.gift-base{left:91px;top:384px;width:192px;height:48px;border:1px solid rgba(255,255,255,.5)}
.spec-table{position:absolute;left:6px;top:6px;right:6px;height:30px;background:var(--white);display:grid;grid-template-columns:repeat(6,1fr);grid-template-rows:1fr 1fr}
.spec-table span{border:1px solid var(--blue);font-size:5px;color:var(--navy);padding:1px}

/* long box */
.long-top{left:355px;top:82px;width:305px;height:50px;background:var(--white)}
.long-band{left:355px;top:149px;width:305px;height:55px}

/* tall box */
.tall{left:672px;top:7px;width:120px;height:317px}
.tall-cap{position:absolute;left:0;top:0;width:100%;height:12px;background:var(--paper)}

/* cross box */
.cross-row{left:828px;top:168px;width:336px;height:84px}
.cross-col{left:960px;top:115px;width:96px;height:197px}

/* case backs */
.caseback{top:250px;width:134px;height:110px}

/* hex strip */
.hex-wrap{left:715px;top:336px;width:437px;height:192px}

/* tags */
.tag{left:34px;width:218px;height:90px}

/* folder */
.folder{left:319px;top:427px;width:293px;height:396px}
.folder-window{position:absolute;left:77px;top:29px;width:108px;height:24px;background:var(--paper);border-radius:3px}

/* bag */
.bag{left:631px;top:576px;width:516px;height:247px}
.bag-handle{left:860px;top:525px}
</style>
</head>
<body>

<!-- Gift box dieline -->
<div class="piece gift-flap-l blue"><span class="brand" style="left:10px;top:30px;font-size:16px;transform:rotate(180deg)">zolt</span></div>
<div class="piece gift-main blue">
  <span class="brand" style="left:66px;top:22px;font-size:24px;transform:rotate(180deg)">zolt</span>
  <p class="fine" style="left:14px;top:90px;width:160px">Crafted for the trend. Digital precision for every day and every night.</p>
  <span class="brand" style="left:40px;top:236px;font-size:40px">zolt</span>
  <span class="url" style="left:56px;top:286px;color:var(--navy)">www.zolt.com</span>
</div>
<div class="piece gift-flap-r blue"></div>
<div class="piece gift-base blue">
  <div class="spec-table">
    <span>Model</span><span>Colour</span><span>Size</span><span>Strap</span><span>Batch</span><span>Date</span>
    <span></span><span></span><span></span><span></span><span></span><span></span>
  </div>
</div>

<!-- Long box -->
<div class="piece long-top">
  <span class="url" style="left:14px;top:20px;color:var(--navy)">www.zolt.com</span>
  <span class="brand" style="left:120px;top:10px;font-size:30px">zolt</span>
</div>
<div class="piece long-band blue">
  <span class="url" style="left:14px;top:22px">www.zolt.com</span>
  <span class="brand" style="left:220px;top:14px;font-size:26px">zolt</span>
</div>

<!-- Tall box -->
<div class="piece tall blue">
  <div class="tall-cap"></div>
  <span class="brand" style="left:72px;top:16px;font-size:18px">zolt</span>
  <span class="url" style="left:40px;top:150px;transform:rotate(90deg)">www.zolt.com</span>
  <span class="brand" style="left:72px;top:292px;font-size:18px">zolt</span>
</div>

<!-- Cross box -->
<div class="piece cross-row blue">
  <p class="fine" style="left:10px;top:24px;width:110px">Trendy digital watch made for bold days and bright nights.</p>
  <span class="url" style="left:240px;top:36px">www.zolt.com</span>
</div>
<div class="piece cross-col blue">
  <span class="brand" style="left:20px;top:82px;font-size:26px">zolt</span>
</div>

<!-- Case backs -->
<div class="piece caseback" style="left:365px" role="img" aria-label="Round engraved steel watch case back">
  <svg width="134" height="110" viewBox="0 0 134 110"><defs><radialGradient id="m1"><stop offset="0" stop-color="#f4f5f6"/><stop offset="1" stop-color="#8e9398"/></radialGradient></defs><circle cx="67" cy="55" r="52" fill="url(#m1)"/><circle cx="67" cy="55" r="34" fill="none" stroke="#7c8288" stroke-width="2"/></svg>
</div>
<div class="piece caseback" style="left:509px" role="img" aria-label="Square engraved steel watch case back">
  <svg width="134" height="110" viewBox="0 0 134 110"><defs><radialGradient id="m2"><stop offset="0" stop-color="#f4f5f6"/><stop offset="1" stop-color="#8e9398"/></radialGradient></defs><rect x="12" y="3" width="110" height="104" rx="20" fill="url(#m2)"/><circle cx="67" cy="55" r="36" fill="none" stroke="#7c8288" stroke-width="2"/></svg>
</div>

<!-- Hexagon tag strip -->
<div class="piece hex-wrap">
  <svg width="437" height="192" viewBox="0 0 437 192">
    <defs>
      <linearGradient id="hb" x1="0" x2="1"><stop offset="0" stop-color="#3fb6ee"/><stop offset="1" stop-color="#0a70b6"/></linearGradient>
      <radialGradient id="ph"><stop offset="0" stop-color="#6b6e72"/><stop offset="1" stop-color="#e9eaeb"/></radialGradient>
    </defs>
    <polygon points="0,46 22,6 72,6 94,46 72,86 22,86" fill="url(#hb)"/>
    <polygon points="80,46 102,6 152,6 174,46 152,86 102,86" fill="#fff"/>
    <polygon points="160,46 182,6 232,6 254,46 232,86 182,86" fill="#fff"/>
    <polygon points="240,46 262,6 312,6 334,46 312,86 262,86" fill="url(#hb)"/>
    <polygon points="320,46 342,6 392,6 414,46 392,86 342,86" fill="url(#hb)"/>
    <polygon points="0,142 22,102 72,102 94,142 72,182 22,182" fill="#fff"/>
    <polygon points="80,142 102,102 152,102 174,142 152,182 102,182" fill="#fff"/>
    <polygon points="160,142 182,102 232,102 254,142 232,182 182,182" fill="#fff"/>
    <polygon points="240,142 262,102 312,102 334,142 312,182 262,182" fill="#fff"/>
    <polygon points="320,142 342,102 392,102 414,142 392,182 342,182" fill="url(#hb)"/>
    <g role="img" aria-label="Photos of Zolt digital and analogue watches">
      <circle cx="127" cy="46" r="30" fill="url(#ph)"/><circle cx="207" cy="46" r="30" fill="url(#ph)"/>
      <circle cx="47" cy="142" r="30" fill="url(#ph)"/><circle cx="127" cy="142" r="30" fill="url(#ph)"/>
      <circle cx="207" cy="142" r="30" fill="url(#ph)"/><circle cx="287" cy="142" r="30" fill="url(#ph)"/>
    </g>
    <text x="20" y="50" font-family="Exo 2, sans-serif" font-size="7" fill="#fff">Digital edge</text>
    <text x="346" y="30" font-family="Exo 2, sans-serif" font-size="7" fill="#fff">www.zolt.com</text>
    <text x="344" y="146" font-family="Exo 2, sans-serif" font-size="6" fill="#fff">Made for trend</text>
  </svg>
</div>

<!-- Tags -->
<div class="piece tag" style="top:547px">
  <svg width="218" height="90" viewBox="0 0 218 90"><polygon points="0,45 20,5 100,5 110,45 100,85 20,85" fill="#1c9ad9"/><polygon points="118,45 128,5 198,5 218,45 198,85 128,85" fill="#1c9ad9"/><rect x="10" y="30" width="92" height="28" fill="#fff"/><rect x="130" y="30" width="76" height="28" fill="#fff"/></svg>
  <span class="brand" style="left:20px;top:32px;font-size:24px">zolt</span>
  <span class="url" style="left:22px;top:66px">www.zolt.com</span>
</div>
<div class="piece tag" style="top:672px">
  <svg width="218" height="90" viewBox="0 0 218 90"><polygon points="0,45 20,5 100,5 110,45 100,85 20,85" fill="#eef3f6"/><polygon points="118,45 128,5 198,5 218,45 198,85 128,85" fill="#eef3f6"/><rect x="10" y="30" width="92" height="28" fill="#1c9ad9"/><rect x="130" y="30" width="76" height="28" fill="#1c9ad9"/></svg>
  <span class="brand" style="left:20px;top:32px;font-size:24px">zolt</span>
  <span class="url" style="left:22px;top:66px;color:var(--navy)">www.zolt.com</span>
</div>

<!-- Folder -->
<div class="piece folder blue">
  <div class="folder-window"></div>
  <p class="fine" style="left:20px;top:90px;width:250px">Zolt trendy digital watches. Light, bold and fresh designs for every wrist and every moment.</p>
  <span class="brand" style="left:160px;top:350px;font-size:28px">zolt</span>
</div>

<!-- Bag -->
<svg class="piece bag-handle" width="80" height="60" viewBox="0 0 80 60"><path d="M10 60 C10 0 70 0 70 60" fill="none" stroke="#0a70b6" stroke-width="3"/></svg>
<div class="piece bag blue">
  <span class="url" style="left:-18px;top:90px;transform:rotate(90deg)">www.zolt.com</span>
  <span class="url" style="left:50px;top:90px;transform:rotate(90deg)">www.zolt.com</span>
  <span class="brand" style="left:220px;top:100px;font-size:48px">zolt</span>
  <span class="url" style="left:360px;top:222px;color:var(--navy)">www.zolt.com</span>
</div>

</body>
</html>
```